Need *Plum Crafted* Events Company Website
Bright Harbor Gatherings Website
Need *Plum Crafted* Events Company Website - Events
Creative Brief
Events
www.brightharborgatherings.example
Bright Harbor Gatherings (BHG) is a multi-dimensional event management firm providing all aspects of support and expertise for any special event. By providing upscale and individualized service, our events are unique and tailored around your personal vision, style and budget.
We provide partial and full-service event coordination services for all types of events; specializing in corporate meetings, conferences, receptions, and everyday social events.
We like unique and captivating web design that illustrates the characteristics of our brand and service offerrings. Our logo speaks to a company that is unique and classy with an edge. DISLIKE: Black or extremely dark backgrounds. Too fancy flash applications, Music or any kind of intro, anything that is too elaborate. LIKE: Easy flow and simplicity. I like the mix of soft neutrals
Feminine
neutral tones
pop of red
complementary tones
right side
www.vowlantern.example
www.quillaffairs.example
Will attached websites that we like later Please use the Fonts from my logo: Will attach files I would like for you to use the accent color on my logo as an special accent only so my logo is not overpowered. I am open to navigation placement but it does not give me that option so I selected what I believe is my personal preference.

```html
<!DOCTYPE html>
<html lang="en">
<head>
<meta charset="utf-8">
<title>Bright Harbor Gatherings — Events</title>
<link rel="stylesheet" href="https://fonts.googleapis.com/css2?family=Great+Vibes&family=Lora:ital,wght@0,400;0,700;1,400;1,700&display=swap">
<style>
  :root{
    --linen:#d9ceb6;
    --linen-dark:#c8bb9d;
    --linen-edge:#b9aa8a;
    --plum:#5f3737;
    --plum-deep:#4a2a2a;
    --olive:#86774a;
    --olive-dark:#6e6139;
    --cream:#f7f1e3;
    --text-dark:#3d2a22;
    --muted:#b99d98;
  }
  *{box-sizing:border-box;margin:0;padding:0}
  html,body{width:1200px;height:799px;overflow:hidden}
  body{background:var(--linen);font-family:"Lora",Georgia,serif;position:relative}
  .canvas{position:relative;width:1200px;height:799px;overflow:hidden;
    background:
      repeating-linear-gradient(0deg,rgba(255,255,255,.06) 0 2px,rgba(0,0,0,.03) 2px 4px),
      repeating-linear-gradient(90deg,rgba(255,255,255,.05) 0 2px,rgba(0,0,0,.03) 2px 4px),
      var(--linen);}
  .edge-band{position:absolute;top:0;bottom:0;left:0;width:106px;background:var(--linen-dark);
    border-right:2px solid var(--linen-edge)}
  .edge-band.right{left:auto;right:0;width:104px;border-right:none;border-left:2px solid var(--linen-edge)}
  .stitch{position:absolute;top:0;bottom:0;width:0;border-left:3px dashed #8d7c5d;opacity:.7}
  .stitch.left{left:112px}
  .stitch.right{left:1106px}

  .sidebar{position:absolute;left:821px;top:0;width:264px;height:799px;
    background:linear-gradient(180deg,var(--plum) 0%,var(--plum-deep) 100%);
    box-shadow:-4px 0 10px rgba(0,0,0,.25),4px 0 10px rgba(0,0,0,.25)}
  .brand{position:absolute;top:150px;left:0;width:100%;text-align:center}
  .brand-mark{width:34px;height:34px;border-radius:50%;border:2px solid var(--cream);margin:0 auto 14px}
  .brand-name{color:var(--cream);font-family:"Lora",Georgia,serif;font-size:22px;font-weight:400;line-height:1.3;padding:0 30px}
  .main-nav{position:absolute;top:420px;left:0;width:100%;text-align:center;list-style:none}
  .main-nav li{font-style:italic;font-weight:700;font-size:17px;letter-spacing:1.5px;color:var(--cream);
    line-height:32px;font-variant:small-caps}
  .connect{position:absolute;top:706px;width:100%;text-align:center;color:var(--muted);
    font-style:italic;font-size:15px}
  .social{position:absolute;top:736px;left:0;width:100%;display:flex;justify-content:center;gap:12px}
  .social span{width:24px;height:24px;background:var(--muted);border-radius:3px;opacity:.8}

  .hero{position:absolute;left:132px;top:29px;width:650px;height:470px;background:#fff;padding:10px;
    box-shadow:0 3px 10px rgba(0,0,0,.35)}
  .hero-photo{position:relative;width:100%;height:100%;
    background:radial-gradient(ellipse at 60% 20%,#f3e6c8 0%,#d9c09a 40%,#a88866 80%,#7d5e45 100%)}
  .tagline{position:absolute;top:96px;left:0;width:100%;text-align:center;
    font-family:"Great Vibes",cursive;font-size:42px;color:#fff;text-shadow:0 2px 4px rgba(0,0,0,.6)}
  .thumbs{position:absolute;left:8px;right:8px;bottom:8px;display:flex;justify-content:space-between}
  .thumb{width:198px;height:146px;border:6px solid #fff;box-shadow:0 2px 6px rgba(0,0,0,.4)}
  .thumb.conference{background:linear-gradient(160deg,#e0c7a3,#9a6a45)}
  .thumb.party{background:linear-gradient(160deg,#b7436a,#5f86b0)}
  .thumb.meeting{background:linear-gradient(160deg,#ece8e2,#8a7a6a)}

  .video{position:absolute;left:137px;top:540px;width:259px;height:192px;
    background:var(--plum);box-shadow:0 3px 8px rgba(0,0,0,.35)}
  .video-brand{position:absolute;left:22px;top:50px;width:110px;color:var(--cream);font-size:14px;line-height:1.3;text-align:center}
  .play{position:absolute;left:148px;top:44px;width:78px;height:78px;border-radius:50%;
    background:radial-gradient(circle at 40% 35%,#8fa552,#4f6425);border:3px solid #3a2020}
  .controls{position:absolute;left:0;bottom:0;width:100%;height:30px;background:#e4e0da;border-top:1px solid #bbb}

  .testimonial{position:absolute;left:427px;top:540px;width:355px;height:180px;
    background:radial-gradient(ellipse at 30% 30%,var(--olive) 0%,var(--olive-dark) 100%);
    box-shadow:0 3px 8px rgba(0,0,0,.35);color:#f1ead6}
  .testimonial h2{position:absolute;left:18px;top:8px;font-family:"Great Vibes",cursive;font-weight:400;font-size:32px}
  .quote-mark{position:absolute;left:12px;top:38px;font-family:"Lora",Georgia,serif;font-size:140px;line-height:1;color:#f1ead6;opacity:.9}
  .testimonial p{position:absolute;left:172px;top:58px;width:168px;font-style:italic;font-size:11.5px;line-height:1.35}
  .testimonial cite{position:absolute;right:16px;bottom:14px;font-size:11px;font-style:italic}

  .copyright{position:absolute;left:137px;top:760px;width:645px;text-align:center;font-size:11px;font-style:italic;color:var(--text-dark)}
</style>
</head>
<body>
<div class="canvas">
  <div class="edge-band"></div>
  <div class="edge-band right"></div>
  <div class="stitch left"></div>
  <div class="stitch right"></div>

  <section class="hero">
    <div class="hero-photo" role="img" aria-label="Elegant banquet hall with chandelier and set tables">
      <div class="tagline">Tailoring the finest events for you...</div>
      <div class="thumbs">
        <div class="thumb conference" role="img" aria-label="Audience at a conference"></div>
        <div class="thumb party" role="img" aria-label="Colourful party celebration"></div>
        <div class="thumb meeting" role="img" aria-label="Corporate meeting around a table"></div>
      </div>
    </div>
  </section>

  <aside class="sidebar">
    <div class="brand">
      <div class="brand-mark"></div>
      <div class="brand-name">Bright Harbor Gatherings</div>
    </div>
    <ul class="main-nav">
      <li>Home</li>
      <li>About Us</li>
      <li>Services</li>
      <li>Contact Us</li>
      <li>Events</li>
      <li>Our Blog</li>
    </ul>
    <div class="connect">Connect with us</div>
    <div class="social"><span></span><span></span><span></span></div>
  </aside>

  <section class="video">
    <div class="video-brand">Bright Harbor Gatherings</div>
    <div class="play">
      <svg width="72" height="72" viewBox="0 0 72 72"><polygon points="28,20 54,36 28,52" fill="#3a2020"/></svg>
    </div>
    <div class="controls">
      <svg width="259" height="30" viewBox="0 0 259 30">
        <polygon points="8,9 18,15 8,21" fill="#555"/>
        <rect x="24" y="9" width="11" height="11" fill="#555"/>
        <rect x="42" y="9" width="12" height="11" fill="#555"/>
        <line x1="62" y1="15" x2="180" y2="15" stroke="#888" stroke-width="3"/>
        <circle cx="96" cy="15" r="5" fill="#666"/>
        <rect x="188" y="9" width="10" height="11" fill="#555"/>
        <line x1="204" y1="15" x2="224" y2="15" stroke="#888" stroke-width="3"/>
        <rect x="232" y="9" width="16" height="11" fill="none" stroke="#555" stroke-width="2"/>
      </svg>
    </div>
  </section>

  <section class="testimonial">
    <h2>Testimonials</h2>
    <div class="quote-mark">&ldquo;</div>
    <p>Lorem ipsum dolor sit amet, consectetur adipiscing elit. Integer at magna purus, vel condimentum diam. Mauris libero dolor, hendrerit eget molestie gravida.</p>
    <cite>~ Della Marchetti</cite>
  </section>

  <footer class="copyright">Copyright © 2011, Bright Harbor Gatherings. All rights reserved.</footer>
</div>
</body>
</html>
```